Verpackungsdesign für hochwertiges Haarparfum
Zielgruppe
Tovel's Method ist eine israelische Firma, die hochqualitative Haarprodukte und Haar Tools verkauft. Unsere Zielgruppe sind Frauen, die viel in Ihr Aussehen investieren und auf Ihr Äußeres sehr Wert legen.
Aufgabenstellung
Wir suchen nach einem Design für unsere zwei neuen Haarparfums. Es sollte teuer aussehen und das Design sollte modern und simpel sein. Die Flachen sind mit Milchglas und das Design wird auf die Flaschen gedruckt. Das Design muss komplett in Englischer Sprache sein.
Die Masse sind:
Höhe 7,7 cm
Umfang 11 cm
Es wird zwei Düfte geben.
1. The Nordic : Deckel wird Silber glänzend
2. The Celtic: Deckel wird Silber matt
Informationen die auf der Flasche sein sollten:
1. Firmen Logo (wird angehängt)
2. Name des Parfüms (The Nordic or the Celtic)
3. Longlasting Hair Fragrance
4. 30 ml
5. Includes essential hair vitamins and minerals
6. Alcohol and salt free

```html
<!DOCTYPE html>
<html lang="en">
<head>
<meta charset="utf-8">
<title>Celtic – Longlasting Hair Fragrance Label</title>
<link rel="stylesheet" href="https://fonts.googleapis.com/css2?family=Figtree:wght@400&family=Fraunces:opsz,wght@144,400&family=Montserrat:wght@400;600&display=swap">
<style>
  :root {
    --page-bg: #ffffff;
    --label-bg: #ececec;
    --label-border: #8a8a8a;
    --ink: #1e1e1e;
    --wreath-gold: #e6c79f;
    --wreath-gold-soft: rgba(230, 199, 159, 0);
  }
  * { margin: 0; padding: 0; box-sizing: border-box; }
  html, body {
    width: 1200px;
    height: 1074px;
    overflow: hidden;
    background: var(--page-bg);
  }
  .canvas {
    position: relative;
    width: 1200px;
    height: 1074px;
  }
  .label {
    position: absolute;
    left: 162px;
    top: 34px;
    width: 876px;
    height: 1005px;
    background: var(--label-bg);
    border: 3px solid var(--label-border);
    color: var(--ink);
    text-align: center;
  }
  .wreath {
    position: absolute;
    left: 73px;
    top: 42px;
    width: 730px;
    height: 646px;
    border-radius: 50% 50% 48% 48%;
    background: radial-gradient(ellipse at 50% 45%, var(--wreath-gold-soft) 52%, var(--wreath-gold) 68%, var(--wreath-gold-soft) 74%);
  }
  .brand {
    position: absolute;
    left: 0;
    right: 0;
    top: 150px;
    display: flex;
    align-items: center;
    justify-content: center;
    gap: 8px;
    font-family: "Montserrat", sans-serif;
    font-weight: 600;
    font-size: 13px;
    letter-spacing: 0.08em;
    text-transform: uppercase;
  }
  .brand-square {
    width: 14px;
    height: 14px;
    background: var(--ink);
  }
  .kicker {
    position: absolute;
    left: 0;
    right: 0;
    top: 264px;
    font-family: "Montserrat", sans-serif;
    font-weight: 400;
    font-size: 27px;
    letter-spacing: 0.08em;
  }
  .product-name {
    position: absolute;
    left: 0;
    right: 0;
    top: 280px;
    font-family: "Fraunces", serif;
    font-weight: 400;
    font-size: 104px;
    line-height: 1.1;
    letter-spacing: -0.01em;
  }
  .tagline {
    position: absolute;
    left: 0;
    right: 0;
    top: 474px;
    font-family: "Montserrat", sans-serif;
    font-weight: 600;
    font-size: 26px;
    line-height: 35px;
    letter-spacing: 0.1em;
  }
  .claims {
    position: absolute;
    left: 0;
    right: 0;
    top: 806px;
    font-family: "Figtree", sans-serif;
    font-size: 20px;
    line-height: 28px;
  }
  .claims p + p { margin-top: 22px; }
  .volume {
    position: absolute;
    left: 0;
    right: 0;
    top: 966px;
    font-family: "Figtree", sans-serif;
    font-size: 21px;
  }
</style>
</head>
<body>
<main class="canvas">
  <section class="label">
    <div class="wreath" role="img" aria-label="Golden laurel wreath of palm leaves framing the product name"></div>
    <div class="brand"><span class="brand-square"></span><span>Tovel's Method</span></div>
    <p class="kicker">perfüme</p>
    <h1 class="product-name">Celtic</h1>
    <p class="tagline">Longlasting<br>Hair Fragrance</p>
    <div class="claims">
      <p>Includes essential hair<br>vitamins and minerals</p>
      <p>Alcohol and salt free</p>
    </div>
    <p class="volume">30 ml</p>
  </section>
</main>
</body>
</html>
```